Business Card Design - Pediatric Dentist

We need a business card for a new dental office. We are a pediatric dentist in Austin Tx. I would like a design that use bright green and if possible light blue.

Target Market(s)

Marketed to young moms

Industry/Entity Type

Dental

Contact Information for Business Card

Marcus Pell DDS
Bramblewood Family Dentistry
428 E. Marlowe Road. Austin TX 78690
(512) 555 0183.

In the back i would like to state "we take most insurances, Tova & Vitacover" & a map

Colors
add136
cadf82
85cae6

```html
<!DOCTYPE html>
<html lang="en">
<head>
<meta charset="utf-8">
<title>Bramblewood Family Dentistry – Business Card</title>
<link rel="stylesheet" href="https://fonts.googleapis.com/css2?family=Tinos&family=Didact+Gothic&display=swap">
<style>
  :root {
    --paper: #ffffff;
    --lime: #aaff00;
    --star-green: #5fe62e;
    --sky: #8eeef4;
    --ink: #111111;
  }
  html, body {
    margin: 0;
    padding: 0;
    width: 1200px;
    height: 702px;
    overflow: hidden;
    background: var(--paper);
  }
  .card {
    position: relative;
    width: 1200px;
    height: 702px;
    overflow: hidden;
    background: var(--paper);
  }
  .card-shapes {
    position: absolute;
    inset: 0;
  }
  .practice-name {
    position: absolute;
    left: 590px;
    top: 68px;
    margin: 0;
    font-family: "Tinos", "Times New Roman", serif;
    font-weight: 400;
    font-size: 72px;
    line-height: 84px;
    color: var(--ink);
  }
  .practice-name span { display: block; }
  .contact {
    position: absolute;
    left: 0;
    width: 1200px;
    top: 428px;
    margin: 0;
    text-align: center;
    font-family: "Didact Gothic", "Helvetica Neue", Arial, sans-serif;
    font-size: 29px;
    line-height: 34px;
    letter-spacing: 0.5px;
    color: var(--ink);
  }
  .contact span { display: block; }
  .contact .dentist { margin-left: 0; }
  .contact .phone { margin-left: 0; }
</style>
</head>
<body>
  <div class="card">
    <svg class="card-shapes" width="1200" height="702" viewBox="0 0 1200 702" aria-hidden="true">
      <circle class="lime-disc" cx="960" cy="332" r="520" fill="var(--lime)"/>
      <rect class="band band-sky" x="0" y="335" width="1200" height="24" fill="var(--sky)"/>
      <rect class="band band-lime" x="0" y="359" width="1200" height="28" fill="var(--lime)"/>
      <rect class="band band-sky" x="0" y="387" width="1200" height="24" fill="var(--sky)"/>
      <circle class="brand-dot" cx="448" cy="190" r="118" fill="var(--star-green)"/>
    </svg>

    <h1 class="practice-name">
      <span>Bramblewood</span>
      <span>Family</span>
      <span>Dentistry</span>
    </h1>

    <p class="contact">
      <span class="dentist">Marcus Pell DDS</span>
      <span class="address">428 E. Marlowe Road. Austin TX 78690</span>
      <span class="phone">p. 512.555 .0183</span>
    </p>
  </div>
</body>
</html>
```